Design a menu for a Pizza company

I need help designing a color menu for a pizza company. It will be a 9x16" trifold menu (3-panel). I would like to include some photos of pizza, salads, subs, sandwiches, drinks, etc. (no clipart). Attached is an example of an existing menu. I need to make the menu full color. We would like to modernize this menu with full color photos like the attached sample menu. The final files should have editable files so I can edit prices and menu items as needed. I prefer CorelDraw graphics software.

Target Market(s)

General public.

Industry/Entity Type

Restaurant

Font styles to use
Sans Serif

Colors
ec1f27
fffefc
9bcb3b

Requirements
Must have
• Must have photos and editable fonts. I will need to be able to edit the contents of the menu after you provide me with the final files.
Nice to have
• It would be nice to have this menu created in CorelDraw X7 or X8.
Should not have
• Should not have clip art or low resolution photos.

```html
<!DOCTYPE html>
<html lang="en">
<head>
<meta charset="utf-8">
<title>Pizza Trifold Menu</title>
<link rel="stylesheet" href="https://fonts.googleapis.com/css2?family=Luckiest+Guy&family=Roboto+Condensed:ital,wght@0,400;0,700;1,400;1,700&display=swap">
<style>
:root{
  --red:#ec1f27;
  --red-dark:#b10f15;
  --cream:#fffefc;
  --green:#9bcb3b;
  --green-deep:#3b7a22;
  --green-dark:#2c5f18;
  --band-green:#3d8a25;
  --ink-green:#2f7d1f;
  --paper:#f3f2ee;
  --stage:#16241c;
}
*{margin:0;padding:0;box-sizing:border-box}
html,body{width:1200px;height:900px;overflow:hidden;background:var(--stage)}
body{font-family:"Roboto Condensed",sans-serif}
.menu{display:flex;width:1200px;height:900px}
.panel{width:400px;height:900px;padding:22px 20px 16px;display:flex;flex-direction:column}
.panel--starters{background:linear-gradient(160deg,#4a8a2a,var(--green-deep) 55%,var(--green-dark));color:var(--cream)}
.panel--subs{background:var(--paper);color:var(--ink-green)}
.panel--pizza{background:radial-gradient(ellipse at 50% 40%,#e3191f,var(--red-dark));color:var(--cream)}

.band{position:relative;height:40px;margin:6px 0 8px;display:flex;align-items:center;border-radius:20px;padding-left:80px;padding-right:10px;flex-shrink:0}
.panel--starters .band,.panel--subs .band{background:var(--red)}
.panel--pizza .band{background:var(--band-green)}
.band .photo{position:absolute;left:-6px;top:50%;transform:translateY(-50%);width:80px;height:54px;border-radius:50%}
.band h2{font-family:"Luckiest Guy",sans-serif;font-weight:400;font-size:25px;line-height:1;letter-spacing:.3px;color:#3f9a2a;text-shadow:-1px -1px 0 var(--cream),1px -1px 0 var(--cream),-1px 1px 0 var(--cream),1px 1px 0 var(--cream);padding-top:4px;flex:1;min-width:0;white-space:nowrap}
.band h2.title--long{font-size:20px}
.band h2.title--longer{font-size:18px}
.panel--pizza .band h2{color:var(--red)}
.band .sizes{display:flex;flex-shrink:0;font-family:"Luckiest Guy",sans-serif;font-size:15px;line-height:1;color:var(--cream);padding-top:3px}
.band .sizes span{text-align:right}
.band .sizes small{font-size:8px;display:block}
.band .note{flex-shrink:0;font-size:10px;font-style:italic;color:var(--cream);text-align:center;line-height:1.1;margin-right:6px}

.photo--app{background:radial-gradient(circle,#e8b866,#b97a2e)}
.photo--side{background:radial-gradient(circle,#f0c878,#c88a3a 60%,#fff 62%)}
.photo--salad{background:radial-gradient(circle,#8cc040,#3f8a22 60%,#d23a2a)}
.photo--sand{background:radial-gradient(circle,#e0b080,#b47a44)}
.photo--super{background:linear-gradient(#e0b879,#d98a8a 50%,#7fb04a)}
.photo--hot{background:linear-gradient(#d9a55c,#8a4a28 50%,#d5b060)}
.photo--parm{background:radial-gradient(circle,#b3422a,#d4a05c)}
.photo--pizza{background:radial-gradient(circle,#d9432c,#e7b057 70%,#c8872e)}
.photo--platter{background:radial-gradient(circle,#c98a5a,#8a5a32)}
.photo--bun{background:radial-gradient(circle,#d9a56a,#6f8a3a)}

.list{list-style:none;padding:0 4px 0 18px}
.item{display:flex;align-items:baseline;font-size:15px;line-height:19.5px;white-space:nowrap}
.item .desc{font-size:9px;font-style:italic;margin-left:4px}
.item--tight{letter-spacing:-.3px}
.item--tight .desc{font-size:8px;letter-spacing:-.2px}
.panel--subs .item .desc{color:var(--red);font-weight:700}
.dots{flex:1;border-bottom:1px solid currentColor;opacity:.55;margin:0 2px;transform:translateY(-4px);min-width:4px}
.price{width:44px;text-align:right;flex-shrink:0;letter-spacing:0}
.price--wide{width:48px}
.intro{font-size:12.5px;font-style:italic;text-align:center;line-height:17px}
.footnote{font-size:12.5px;font-style:italic;text-align:center;margin-top:auto;padding:0 20px 6px;line-height:17px}
.gyro{margin-top:8px}
.extras{text-align:center;color:var(--red);font-size:12.5px;margin-top:6px;line-height:16px}
.extras strong{font-style:italic}
.item--sub{font-size:9px;font-style:italic;line-height:12px;padding-bottom:2px}
.spacer{height:8px}
</style>
</head>
<body>
<main class="menu">

  <section class="panel panel--starters">
    <div class="band"><div class="photo photo--app" role="img" aria-label="Photo of mozzarella sticks and fried appetizers"></div><h2>Appetizers</h2></div>
    <ul class="list">
      <li class="item">Mozzarella Sticks<span class="desc">served with Marinara Sauce</span><span class="dots"></span><span class="price">6.49</span></li>
      <li class="item">Chicken Tenders<span class="desc">served with Honey Mustard Sauce</span><span class="dots"></span><span class="price">6.49</span></li>
      <li class="item">Jalapeno Peppers<span class="desc">served with Marinara Sauce</span><span class="dots"></span><span class="price">6.49</span></li>
      <li class="item">8-Piece Buffalo Wings<span class="desc">served with Blue Cheese Sauce</span><span class="dots"></span><span class="price">6.99</span></li>
      <li class="item">Fried Mushroom<span class="desc">served with Ranch Dressing</span><span class="dots"></span><span class="price">6.49</span></li>
    </ul>
    <div class="spacer"></div>
    <div class="band"><div class="photo photo--side" role="img" aria-label="Photo of onion rings on a plate"></div><h2>Side Orders</h2></div>
    <ul class="list">
      <li class="item">French Fries<span class="dots"></span><span class="price">2.49</span></li>
      <li class="item">Onion Rings<span class="dots"></span><span class="price">2.49</span></li>
      <li class="item">Garlic Bread<span class="dots"></span><span class="price">1.99</span></li>
      <li class="item">Garlic Bread with Cheese<span class="dots"></span><span class="price">2.99</span></li>
      <li class="item">Cole Slaw<span class="dots"></span><span class="price">1.99</span></li>
    </ul>
    <div class="spacer"></div>
    <div class="band"><div class="photo photo--salad" role="img" aria-label="Photo of a fresh garden salad"></div><h2 class="title--long">Garden Fresh Salads</h2></div>
    <p class="intro">Choice of Dressing:<br>Ranch - French - Italian - Blue Cheese - Thousand Island</p>
    <ul class="list">
      <li class="item">Garden Salad<span class="dots"></span><span class="price">4.49</span></li>
      <li class="item">Chef Salad<span class="desc">(ham, salami, cheese &amp; hard boiled egg)</span><span class="dots"></span><span class="price">7.99</span></li>
      <li class="item">Greek Salad<span class="dots"></span><span class="price">7.99</span></li>
      <li class="item">Grilled Chicken Salad<span class="desc">(with cheese &amp; hard boiled egg)</span><span class="dots"></span><span class="price">7.99</span></li>
      <li class="item">Gyro Salad (Beef or Chicken)<span class="dots"></span><span class="price">7.99</span></li>
      <li class="item">Tuna Salad<span class="dots"></span><span class="price">7.99</span></li>
    </ul>
    <div class="spacer"></div>
    <div class="band"><div class="photo photo--sand" role="img" aria-label="Photo of a roast beef sandwich"></div><h2>Sandwiches</h2></div>
    <p class="intro">All available on Wheat, Rye, White Bread</p>
    <ul class="list">
      <li class="item">Ham &amp; Cheese with LTM<span class="dots"></span><span class="price">5.49</span></li>
      <li class="item">Roast Beef with LTM<span class="dots"></span><span class="price">5.99</span></li>
      <li class="item">Tuna Salad with LTM<span class="dots"></span><span class="price">5.99</span></li>
      <li class="item">Turkey, Ham, Cheese with LTM<span class="dots"></span><span class="price">5.99</span></li>
      <li class="item">Turkey &amp; Cheese with LTM<span class="dots"></span><span class="price">5.99</span></li>
      <li class="item">Tuna Salad<span class="dots"></span><span class="price">5.99</span></li>
    </ul>
    <p class="footnote">*Consuming raw or undercooked meats may increase your risk of foodborne illness.</p>
  </section>

  <section class="panel panel--subs">
    <div class="band"><div class="photo photo--super" role="img" aria-label="Photo of a cold cut sub"></div><h2>Super Subs</h2><span class="note">Served<br>Cold</span><span class="sizes"><span style="width:34px">8"</span><span style="width:42px">12"</span></span></div>
    <ul class="list">
      <li class="item item--tight">Italian Cold Cut<span class="desc">(ham, salami, cheese, LT, onion, HP, OV)</span><span class="dots"></span><span class="price">6.99</span><span class="price">9.99</span></li>
      <li class="item item--tight">American Hero<span class="desc">(turkey, roast beef, American cheese, LTM)</span><span class="dots"></span><span class="price">6.99</span><span class="price">9.99</span></li>
      <li class="item">Virginia Cold Cut<span class="desc">(ham, turkey, cheese, LTM)</span><span class="dots"></span><span class="price">6.99</span><span class="price">9.99</span></li>
      <li class="item">Tuna Salad<span class="desc">(with LTM)</span><span class="dots"></span><span class="price">6.99</span><span class="price">9.99</span></li>
      <li class="item">Ham &amp; Cheese<span class="desc">(with LTM)</span><span class="dots"></span><span class="price">6.99</span><span class="price">9.99</span></li>
      <li class="item">Turkey Sub<span class="desc">(with LTM)</span><span class="dots"></span><span class="price">6.99</span><span class="price">9.99</span></li>
      <li class="item">Club Sub<span class="desc">(turkey, ham, bacon, LTM)</span><span class="dots"></span><span class="price">6.99</span><span class="price">9.99</span></li>
      <li class="item">Roast Beef<span class="desc">(with LTM)</span><span class="dots"></span><span class="price">6.99</span><span class="price">9.99</span></li>
    </ul>
    <div class="band"><div class="photo photo--hot" role="img" aria-label="Photo of a hot steak sub"></div><h2>Hot Subs</h2><span class="sizes"><span style="width:34px">8"</span><span style="width:42px">12"</span></span></div>
    <ul class="list">
      <li class="item">Steak &amp; Cheese<span class="desc">(with grilled onion, LTM)</span><span class="dots"></span><span class="price">6.99</span><span class="price">9.99</span></li>
      <li class="item">Steak &amp; Mushroom<span class="desc">(with grilled onion, LTM)</span><span class="dots"></span><span class="price">6.99</span><span class="price">9.99</span></li>
      <li class="item">Steak<span class="desc">(with green peppers, grilled onion, LTM)</span><span class="dots"></span><span class="price">6.99</span><span class="price">9.99</span></li>
      <li class="item">Steak<span class="desc">(with onions, pizza sauce)</span><span class="dots"></span><span class="price">6.99</span><span class="price">9.99</span></li>
      <li class="item item--tight">Billy Dooley<span class="desc">(w/ steak, grilled onion, green peppers, egg, LTM)</span><span class="dots"></span><span class="price">6.99</span><span class="price">9.99</span></li>
      <li class="item">Tom Dooley<span class="desc">(with ham, hamburger, egg, LTM)</span><span class="dots"></span><span class="price">6.99</span><span class="price">9.99</span></li>
      <li class="item">Hot Sam<span class="desc">(with ham, bacon, egg, LTM)</span><span class="dots"></span><span class="price">6.99</span><span class="price">9.99</span></li>
      <li class="item">*Cheeseburger Sub<span class="desc">(with LTM)</span><span class="dots"></span><span class="price">6.99</span><span class="price">9.99</span></li>
      <li class="item">Pastrami<span class="desc">(with LTM)</span><span class="dots"></span><span class="price">6.99</span><span class="price">9.99</span></li>
      <li class="item item--tight">Veggie Sub<span class="desc">(w/ olive, green pepper, onion, mushroom, cheese, LTM)</span><span class="dots"></span><span class="price">6.99</span><span class="price">9.99</span></li>
      <li class="item">B. L. T.<span class="desc">(with mayonnaise)</span><span class="dots"></span><span class="price">6.99</span><span class="price">9.99</span></li>
      <li class="item">Crab Cake<span class="desc">(with LTM)</span><span class="dots"></span><span class="price">6.99</span><span class="price">9.99</span></li>
      <li class="item">Fish Fillet<span class="desc">(with LTM)</span><span class="dots"></span><span class="price">6.99</span><span class="price">9.99</span></li>
      <li class="item">Chicken Fillet<span class="desc">(with LTM)</span><span class="dots"></span><span class="price">6.99</span><span class="price">9.99</span></li>
    </ul>
    <div class="band"><div class="photo photo--parm" role="img" aria-label="Photo of a meatball parmigiana sub"></div><h2 class="title--longer">Parmigiana Subs</h2><span class="sizes"><span style="width:34px">8"</span><span style="width:42px">12"</span></span></div>
    <ul class="list">
      <li class="item">Meatball Parmigiana<span class="dots"></span><span class="price">6.99</span><span class="price">9.99</span></li>
      <li class="item">Italian Sausage Parmigiana<span class="dots"></span><span class="price">6.99</span><span class="price">9.99</span></li>
      <li class="item item--tight">Italian Sausage &amp; Green Peppers Parmigiana<span class="dots"></span><span class="price">6.99</span><span class="price">9.99</span></li>
      <li class="item">Chicken Parmigiana<span class="dots"></span><span class="price">6.99</span><span class="price">9.99</span></li>
      <li class="item">Veal Parmigiana<span class="dots"></span><span class="price">6.99</span><span class="price">9.99</span></li>
      <li class="item">Eggplant Parmigiana<span class="dots"></span><span class="price">6.99</span><span class="price">9.99</span></li>
      <li class="item gyro">GYRO Sandwich on Pita Bread<span class="desc">(Chicken or Beef)</span><span class="dots"></span><span class="price">7.99</span></li>
    </ul>
    <p class="extras"><strong>Additional on Subs:</strong><br>Mushroom, Green Peppers ___1.25 &nbsp; Extra Meat ___3.99 &nbsp;Cheese ___1.25</p>
  </section>

  <section class="panel panel--pizza">
    <div class="band"><div class="photo photo--pizza" role="img" aria-label="Photo of a pepperoni pizza"></div><h2>Pizza</h2><span class="sizes"><span style="width:36px">7"<small>mini</small></span><span style="width:44px">10"S</span><span style="width:44px">13"M</span><span style="width:46px">16"L</span></span></div>
    <ul class="list">
      <li class="item">Plain (Cheese)<span class="dots"></span><span class="price">4.49</span><span class="price">6.99</span><span class="price">9.49</span><span class="price price--wide">10.99</span></li>
      <li class="item">Pepperoni<span class="dots"></span><span class="price">4.49</span><span class="price">7.99</span><span class="price">10.49</span><span class="price price--wide">12.99</span></li>
      <li class="item">Sausage<span class="dots"></span><span class="price">4.49</span><span class="price">7.99</span><span class="price">10.49</span><span class="price price--wide">12.99</span></li>
      <li class="item">Hawaiian Pineapple<span class="dots"></span><span class="price">4.49</span><span class="price">7.99</span><span class="price">10.49</span><span class="price price--wide">12.99</span></li>
      <li class="item">Meatball<span class="dots"></span><span class="price">4.49</span><span class="price">7.99</span><span class="price">10.49</span><span class="price price--wide">12.99</span></li>
      <li class="item">Ham<span class="dots"></span><span class="price">4.49</span><span class="price">7.99</span><span class="price">10.49</span><span class="price price--wide">12.99</span></li>
      <li class="item">Ground Beef<span class="dots"></span><span class="price">4.49</span><span class="price">7.99</span><span class="price">10.49</span><span class="price price--wide">12.99</span></li>
      <li class="item">Green Peppers<span class="dots"></span><span class="price">4.49</span><span class="price">7.99</span><span class="price">10.49</span><span class="price price--wide">12.99</span></li>
      <li class="item">Onion<span class="dots"></span><span class="price">4.49</span><span class="price">7.99</span><span class="price">10.49</span><span class="price price--wide">12.99</span></li>
      <li class="item">Black Olives<span class="dots"></span><span class="price">4.49</span><span class="price">7.99</span><span class="price">10.49</span><span class="price price--wide">12.99</span></li>
      <li class="item">Mushroom<span class="dots"></span><span class="price">4.49</span><span class="price">7.99</span><span class="price">10.49</span><span class="price price--wide">12.99</span></li>
      <li class="item">Bacon<span class="dots"></span><span class="price">4.49</span><span class="price">7.99</span><span class="price">10.49</span><span class="price price--wide">12.99</span></li>
      <li class="item">Anchovies<span class="dots"></span><span class="price">4.49</span><span class="price">7.99</span><span class="price">10.49</span><span class="price price--wide">12.99</span></li>
      <li class="item">Salami<span class="dots"></span><span class="price">4.49</span><span class="price">7.99</span><span class="price">10.49</span><span class="price price--wide">12.99</span></li>
      <li class="item">Pepperoni-Mushroom-</li>
      <li class="item">Sausage-Onion<span class="dots"></span><span class="price">10.49</span><span class="price">13.99</span><span class="price price--wide">17.99</span></li>
      <li class="item">Mama Mia Delight<span class="dots"></span><span class="price">8.25</span><span class="price">13.25</span><span class="price">16.95</span><span class="price price--wide">19.99</span></li>
      <li class="item item--sub">Pepperoni, Mushroom, Sausage, Onion, Ham, Salami, Green Pepper, Meatball</li>
      <li class="item">White Pizza<span class="desc">(w/ Butter &amp; Garlic)</span><span class="dots"></span><span class="price">4.99</span><span class="price">7.99</span><span class="price">10.49</span><span class="price price--wide">12.99</span></li>
      <li class="item">Extra Topping<span class="dots"></span><span class="price">0.99</span><span class="price">1.89</span><span class="price">1.99</span><span class="price price--wide">2.20</span></li>
    </ul>
    <div class="spacer"></div>
    <div class="band"><div class="photo photo--platter" role="img" aria-label="Photo of a sandwich platter"></div><h2 class="title--long">Sandwich Platters</h2></div>
    <ul class="list">
      <li class="item">Fresh Roast Beef on Jumbo Bun<span class="desc">(w/ FF &amp; med. drink)</span><span class="dots"></span><span class="price">8.99</span></li>
      <li class="item">*1/2 lb. Cheeseburger<span class="desc">(w/ FF &amp; med. drink)</span><span class="dots"></span><span class="price">8.99</span></li>
      <li class="item item--tight">BBQ Special on Jumbo Bun<span class="desc">(w/ FF, cole slaw &amp; med. drink)</span><span class="dots"></span><span class="price">8.99</span></li>
      <li class="item">Fish Fillet on Sesame Bun<span class="desc">(w/ FF &amp; med. drink)</span><span class="dots"></span><span class="price">8.99</span></li>
      <li class="item">Crab Cake on Sesame Bun<span class="desc">(w/ FF &amp; med. drink)</span><span class="dots"></span><span class="price">8.99</span></li>
      <li class="item item--tight">Gyro Sandwich Beef or Chicken<span class="desc">(w/ FF &amp; med. drink)</span><span class="dots"></span><span class="price">8.99</span></li>
    </ul>
    <div class="spacer"></div>
    <div class="band"><div class="photo photo--bun" role="img" aria-label="Photo of a sandwich on a sesame bun"></div><h2>Sandwiches</h2><span class="note">Served on<br>Sesame Bun</span></div>
    <ul class="list">
      <li class="item">Roast Beef<span class="desc">(w/ LTM)</span><span class="dots"></span><span class="price">4.99</span></li>
      <li class="item">Tuna Salad<span class="dots"></span><span class="price">4.99</span></li>
      <li class="item">Bar-B-Que with Cole Slaw<span class="dots"></span><span class="price">4.99</span></li>
      <li class="item">Grilled Chicken Breast<span class="dots"></span><span class="price">4.99</span></li>
      <li class="item">*Cheeseburger<span class="dots"></span><span class="price">3.75</span></li>
    </ul>
  </section>

</main>
</body>
</html>
```